Baby Shower Invitation for Vectored Image Provided

Corinne & Dorian's Baby Shower - Black/White/Gold Colors preferred
Please use the vectored portrait image attached. I'd like us on the lower right side of the invitation.
Can be horizontal or vertical layout.
The second image attached has the information needed for you to complete.
I don't want that style copied, it is just an example.

```html
<!DOCTYPE html>
<html lang="en">
<head>
<meta charset="utf-8">
<title>Oh Boy! Couples Baby Shower Invitation</title>
<link href="https://fonts.googleapis.com/css2?family=Sofia&family=Yesteryear&family=Bebas+Neue&family=Oswald:wght@300;500&display=swap" rel="stylesheet">
<style>
  :root {
    --page: #f2f2f2;
    --board: #3a3a3a;
    --board-light: #444444;
    --chalk: #f4f4f4;
    --yellow: #f2e40c;
    --green: #1f9a4c;
    --portrait-a: #5a5048;
    --portrait-b: #2a2a2a;
  }
  * { margin: 0; padding: 0; box-sizing: border-box; }
  html, body { width: 1200px; height: 1200px; overflow: hidden; }
  body { background: var(--page); position: relative; }

  .invitation {
    position: absolute; left: 120px; top: 304px;
    width: 960px; height: 590px;
    background: radial-gradient(ellipse at 40% 30%, var(--board-light), var(--board) 70%);
    color: var(--chalk);
  }
  .abs { position: absolute; text-align: center; }

  .headline {
    left: 40px; top: 40px; width: 320px;
    font-family: "Sofia", cursive; font-size: 72px; line-height: 1;
    color: var(--yellow); text-align: left; padding-left: 24px;
  }
  .tagline {
    left: 40px; top: 138px; width: 320px;
    font-family: "Sofia", cursive; font-size: 42px; line-height: 48px;
  }
  .dot-row { left: 40px; top: 276px; }

  .portrait {
    position: absolute; left: 92px; top: 316px; width: 260px; height: 274px;
    background: linear-gradient(160deg, var(--portrait-a), var(--portrait-b));
  }

  .frame { position: absolute; left: 436px; top: 42px; }

  .intro {
    left: 456px; top: 92px; width: 440px;
    font-family: "Yesteryear", cursive; font-size: 20px;
  }
  .names {
    left: 456px; top: 132px; width: 440px;
    font-family: "Bebas Neue", sans-serif; font-size: 56px; letter-spacing: 2px;
    color: var(--yellow); line-height: 1;
  }
  .names .amp { color: var(--green); font-family: "Sofia", cursive; font-size: 46px; padding: 0 12px; }
  .join {
    left: 456px; top: 208px; width: 440px;
    font-family: "Sofia", cursive; font-size: 26px;
  }
  .join .dots { letter-spacing: 3px; font-family: "Oswald", sans-serif; font-size: 16px; vertical-align: middle; }

  .schedule { position: absolute; left: 496px; top: 268px; }
  .when {
    top: 282px; width: 170px;
    font-family: "Oswald", sans-serif; font-weight: 500; font-size: 29px; line-height: 34px;
  }
  .when.date { left: 494px; }
  .when.time { left: 682px; font-size: 31px; }

  .venue {
    left: 456px; top: 368px; width: 440px;
    font-family: "Oswald", sans-serif; font-weight: 300; font-size: 17px; line-height: 25px;
  }
  .rsvp {
    left: 456px; top: 428px; width: 440px;
    font-family: "Bebas Neue", sans-serif; font-size: 28px; letter-spacing: 1px;
  }
  .rsvp .g { color: var(--green); }
  .rsvp .y { color: var(--yellow); }
  .reply {
    left: 456px; top: 462px; width: 440px;
    font-family: "Yesteryear", cursive; font-size: 17px; line-height: 22px;
  }
</style>
</head>
<body>
  <div class="invitation">
    <div class="abs headline">Oh Boy!</div>
    <div class="abs tagline">A little man<br>is on his way!</div>

    <svg class="abs dot-row" width="320" height="14" viewBox="0 0 320 14">
      <g fill="none" stroke="#f4f4f4" stroke-width="2">
        <circle cx="6" cy="7" r="4"/><circle cx="30" cy="7" r="4"/><circle cx="54" cy="7" r="4"/>
        <circle cx="78" cy="7" r="4"/><circle cx="102" cy="7" r="4"/><circle cx="126" cy="7" r="4"/>
        <circle cx="150" cy="7" r="4"/><circle cx="174" cy="7" r="4"/><circle cx="198" cy="7" r="4"/>
        <circle cx="222" cy="7" r="4"/><circle cx="246" cy="7" r="4"/><circle cx="270" cy="7" r="4"/>
        <circle cx="294" cy="7" r="4"/><circle cx="314" cy="7" r="4"/>
      </g>
    </svg>

    <div class="portrait" role="img" aria-label="Illustrated portrait of the expecting couple with a bunch of chalk-drawn balloons"></div>

    <svg class="frame" width="480" height="506" viewBox="0 0 480 506">
      <g fill="none" stroke="#f4f4f4">
        <path stroke-width="3" d="M30,6 Q240,20 450,6 Q456,30 474,36 L470,470 Q456,476 450,500 Q240,486 30,500 Q24,476 6,470 L10,36 Q24,30 30,6 Z"/>
        <path stroke-width="2" d="M40,20 Q240,32 440,20 Q446,40 460,46 L456,460 Q444,466 440,486 Q240,474 40,486 Q36,466 24,460 L20,46 Q34,40 40,20 Z"/>
      </g>
    </svg>

    <div class="abs intro">It's a Couples Baby Shower to Hornor</div>
    <div class="abs names">CORINNE<span class="amp">&amp;</span>DORIAN</div>
    <div class="abs join"><span class="dots">······</span> Please join us <span class="dots">······</span></div>

    <svg class="schedule" width="360" height="92" viewBox="0 0 360 92">
      <g stroke="#f4f4f4" stroke-width="3" stroke-linecap="round" stroke-dasharray="0.1 6">
        <line x1="2" y1="2" x2="358" y2="2"/>
        <line x1="2" y1="89" x2="358" y2="89"/>
        <line x1="176" y1="6" x2="176" y2="86"/>
      </g>
    </svg>
    <div class="abs when date">SATURDAY<br>SEPT 1, 2018</div>
    <div class="abs when time">11.30 AM<br>2.30 PM</div>

    <div class="abs venue">THE WILLOWMERE<br>4172 CALDER ST. RALEIGH, NC</div>
    <div class="abs rsvp"><span class="g">RS</span><span class="y">VP</span></div>
    <div class="abs reply">To Dorian at 555-014-2283<br>by August 20th</div>
  </div>
</body>
</html>
```